Mirabo & Orvan Automotive Repair Shop. Need a new website design.

We specialize in Mirabo & Orvan auto repair, but also work on other Asian import vehicles. We have been in business for 7 years and pride ourselves on high quality auto repair that is fixed right the first time. Would like the automotive repair website to incorporate the colors black, red and white if possible and have our logo and some Mirabo and Orvan vehicles included in the website.

Target Market(s)

Mirabo & Orvan vehicle owners

Industry/Entity Type

Automotive Repair

Coding

Coded - Design and coding required

Number of Pages Required

5+ page

Colors
EB3D1F
EC4F4E
F09395
F8D3D4
FCEDEE

Requirements
Must have
• Home, Services, Contact Us, Schedule appointment, and a gallery tab that I can add shop pictures to when completed.
Nice to have
• Would like to see example pictures of job next to each service listed.
Should not have
• Service not related to auto repair. Ex. auto detailing, towing, car wash

```html
<!DOCTYPE html>
<html lang="en">
<head>
<meta charset="utf-8">
<title>Kestrel Automotive – Contact</title>
<link href="https://fonts.googleapis.com/css2?family=Fira+Sans+Extra+Condensed:ital,wght@0,500;0,700;1,400;1,500&family=Open+Sans:ital,wght@0,400;0,600;0,700;1,400&display=swap" rel="stylesheet">
<style>
:root{
  --red:#e5090f;
  --red-dark:#b80006;
  --black:#0b0b0b;
  --ink:#111;
  --text:#333;
  --muted:#8a8a8a;
  --line:#cfcfcf;
  --paper:#fff;
  --soft:#f5f5f5;
  --footer:#161616;
}
*{margin:0;padding:0;box-sizing:border-box}
html,body{width:758px;height:1200px;overflow:hidden;background:var(--paper)}
body{position:relative;font-family:"Open Sans",sans-serif;color:var(--text)}
.abs{position:absolute}

/* header */
.header{left:0;top:0;width:758px;height:77px;background:var(--black)}
.brand{left:78px;top:22px;display:flex;align-items:center;gap:5px}
.brand-dot{width:14px;height:14px;border-radius:50%;background:var(--red)}
.brand-name{font-family:"Fira Sans Extra Condensed",sans-serif;font-weight:700;font-size:17px;color:var(--paper);line-height:1;letter-spacing:.5px}
.brand-sub{left:97px;top:41px;font-family:"Fira Sans Extra Condensed",sans-serif;font-weight:700;font-size:9px;color:var(--paper);letter-spacing:1.5px}
.perk{display:flex;align-items:center;gap:5px;top:13px}
.perk-icon{width:23px;height:23px;border-radius:50%;border:1.5px solid #bbb;background:#2a2a2a;display:flex;align-items:center;justify-content:center}
.perk-text{font-family:"Fira Sans Extra Condensed",sans-serif;font-style:italic;font-size:9.5px;color:#eee;line-height:1.1}
.perk-text b{color:var(--red);font-weight:500}
.stars{color:var(--red);font-size:10px;font-style:normal}
.nav{top:60px;left:367px;display:flex;gap:20px;font-size:7px;font-weight:700;color:var(--paper);letter-spacing:.1px}
.nav .active{color:var(--red)}
.header-rule{left:0;top:75px;width:215px;height:2px;background:var(--red)}

/* hero */
.hero{left:0;top:77px;width:758px;height:199px;background:linear-gradient(90deg,#6d6e73 0%,#8c95a3 45%,#b9bec6 75%,#d7d9dc 100%)}
.hero-red{left:0;top:77px}
.hero-label{left:104px;top:144px;font-family:"Fira Sans Extra Condensed",sans-serif;font-size:7px;color:var(--paper);letter-spacing:.5px}
.hero-title{left:70px;top:157px;font-family:"Fira Sans Extra Condensed",sans-serif;font-weight:700;font-size:31px;color:var(--paper);line-height:1}
.hero-copy{left:70px;top:195px;width:200px;font-size:7px;line-height:10px;color:var(--paper)}

/* form card */
.card{left:72px;top:350px;width:347px;height:320px;border:1px solid var(--line);background:var(--paper)}
.eyebrow{left:94px;top:381px;display:flex;align-items:center;gap:7px;font-family:"Fira Sans Extra Condensed",sans-serif;font-weight:500;font-size:7px;color:var(--red);letter-spacing:.4px}
.eyebrow i{display:block;width:25px;height:1px;background:var(--red)}
.card-title{left:94px;top:396px;font-family:"Fira Sans Extra Condensed",sans-serif;font-weight:700;font-size:23px;color:var(--ink);line-height:1}
.card-copy{left:94px;top:432px;width:220px;font-size:7px;line-height:11.5px;color:var(--text)}
.field{border:1px solid var(--line);display:flex;align-items:center;justify-content:space-between;padding:0 9px 0 11px;font-family:"Fira Sans Extra Condensed",sans-serif;font-style:italic;font-size:7.5px;color:var(--muted)}
.field.filled{border-color:#333;color:var(--ink);font-weight:500}
.field-icon{width:14px;height:14px;border-radius:50%;border:1px solid #999;display:flex;align-items:center;justify-content:center}
.field.area{align-items:flex-start;padding-top:9px}
.submit{left:94px;top:609px;width:117px;height:28px}
.submit-label{left:94px;top:609px;width:117px;height:28px;display:flex;align-items:center;justify-content:center;gap:5px;font-family:"Fira Sans Extra Condensed",sans-serif;font-weight:700;font-size:8px;color:var(--paper);letter-spacing:.3px}

/* info column */
.lead{left:448px;top:350px;white-space:nowrap;font-family:"Fira Sans Extra Condensed",sans-serif;font-style:italic;font-size:13px;line-height:14px;color:var(--ink)}
.lead u{color:var(--red)}
.lead-copy{left:448px;top:386px;font-size:7px;color:var(--text)}
.touch-title{left:448px;top:422px;font-family:"Fira Sans Extra Condensed",sans-serif;font-weight:700;font-size:23px;line-height:23px;color:var(--ink)}
.touch-copy{left:448px;top:474px;width:190px;font-size:7px;line-height:11.5px;color:var(--text)}
.contact-row{left:448px;display:flex;align-items:center;gap:7px;font-size:7px;line-height:9px;color:var(--text)}
.contact-icon{width:22px;height:22px;border-radius:50%;background:var(--red);display:flex;align-items:center;justify-content:center;flex:none}
.contact-row.big{font-size:10.5px;line-height:12px}
.socials{display:flex;gap:3px}
.social{width:18px;height:18px;border-radius:50%;border:1px solid var(--ink);display:flex;align-items:center;justify-content:center;font-size:6px;font-weight:700;color:var(--ink)}

/* map */
.band-soft{left:0;top:785px;width:758px;height:163px;background:var(--soft)}
.map{left:73px;top:700px;width:616px;height:207px;background:linear-gradient(135deg,#ece9e3 0%,#e6e3dc 40%,#efe8d8 70%,#e9e6e0 100%);box-shadow:0 2px 4px rgba(0,0,0,.25)}
.map-card{left:89px;top:715px;width:121px;height:47px;background:var(--paper);box-shadow:0 1px 3px rgba(0,0,0,.25);padding:6px 7px;font-size:5px;line-height:7.5px;color:#333}
.map-card b{font-size:5.2px;color:#111}
.map-card .link{color:#1a73e8}
.map-dir{left:182px;top:721px;font-size:4.5px;color:#1a73e8;text-align:center}
.zoom{left:665px;top:870px;width:15px;height:31px;background:var(--paper);box-shadow:0 1px 2px rgba(0,0,0,.3);font-size:9px;color:#555;text-align:center;line-height:15px}

/* footer */
.footer{left:0;top:948px;width:758px;height:252px;background:var(--footer)}
.foot-brand{left:72px;top:1030px;display:flex;align-items:center;gap:6px}
.foot-brand .brand-name{font-size:20px}
.foot-brand-sub{left:92px;top:1053px;font-family:"Fira Sans Extra Condensed",sans-serif;font-weight:700;font-size:10px;color:var(--paper);letter-spacing:1.6px}
.badge{background:var(--paper)}
.foot-title{font-family:"Fira Sans Extra Condensed",sans-serif;font-weight:700;font-size:12.5px;color:var(--red);top:985px}
.foot-links{left:232px;top:1012px;display:flex;flex-direction:column;gap:9.5px;font-size:7px;line-height:10.5px;color:#e4e4e4}
.foot-row{left:320px;display:flex;align-items:center;gap:9px;font-size:7px;line-height:10px;color:#e4e4e4}
.foot-icon{width:19px;height:19px;border-radius:50%;background:#d9d9d9;display:flex;align-items:center;justify-content:center;flex:none}
.foot-row em{font-style:normal;color:var(--red)}
.foot-map{left:502px;top:988px;width:186px;height:130px;background:linear-gradient(160deg,#eef0f2 0%,#e4e8ea 55%,#efe9dc 100%);clip-path:polygon(33px 0,100% 0,100% 100%,0 100%,0 33px)}
.foot-social{left:96px;top:1171px;display:flex;gap:3px}
.foot-social .social{border-color:#999;background:#333;color:#eee}
.bottom-bar{left:0;top:1173px}
.copyright{right:68px;top:1182px;font-size:7px;font-weight:600;color:var(--paper)}
</style>
</head>
<body>

<!-- header -->
<div class="abs header"></div>
<div class="abs brand"><span class="brand-dot"></span><span class="brand-name">KESTREL</span></div>
<div class="abs brand-sub">AUTOMOTIVE</div>

<div class="abs perk" style="left:328px">
  <div class="perk-icon"><svg width="11" height="11" viewBox="0 0 12 12"><circle cx="6" cy="5" r="3.5" fill="none" stroke="#ddd" stroke-width="1.2"/><path d="M4 8l-1 3 3-1.5L9 11 8 8" fill="none" stroke="#ddd" stroke-width="1"/></svg></div>
  <div class="perk-text"><span class="stars">★★★★★</span><br>5 Star Service</div>
</div>
<div class="abs perk" style="left:452px">
  <div class="perk-icon"><svg width="11" height="11" viewBox="0 0 12 12"><path d="M2 2l8 8M10 2L2 10" stroke="#ddd" stroke-width="1.4"/></svg></div>
  <div class="perk-text">Quality Service<br><b>Guarantee</b></div>
</div>
<div class="abs perk" style="left:582px">
  <div class="perk-icon"><svg width="11" height="11" viewBox="0 0 12 12"><path d="M3 1.5l2 2.5-1.2 1.2a6 6 0 0 0 3 3L8 7l2.5 2-1.2 1.8C5.5 10.5 1.5 6.5 1.2 2.7z" fill="#ddd"/></svg></div>
  <div class="perk-text">Call Us For Booking<br><b>555.640.2218</b></div>
</div>

<nav class="abs nav">
  <span>HOME</span><span>ABOUT US</span><span>SERVICES ⌄</span><span>GALLERY</span><span>TESTIMONIALS</span><span class="active">CONTACT US</span>
</nav>
<div class="abs header-rule"></div>
<svg class="abs" style="left:210px;top:50px" width="30" height="28"><polygon points="20,0 27,0 7,27 0,27" fill="var(--red)"/><polygon points="25,4 29,4 12,27 8,27" fill="#ddd"/></svg>

<!-- hero -->
<div class="abs hero" role="img" aria-label="Photo of a clean auto repair workshop with lifts and tool benches"></div>
<svg class="abs hero-red" width="758" height="199"><polygon points="0,0 168,0 60,199 0,199" fill="rgba(229,9,15,.45)"/><polygon points="168,0 380,0 290,199 60,199" fill="rgba(229,9,15,.3)"/></svg>
<div class="abs hero-label">CONTACT</div>
<div class="abs hero-title">Contact Us Today!</div>
<div class="abs hero-copy">Quisque lorem neque, ultricies eget risus quis, fringilla interdum augue. Donec sollicitudin in ante sed consequat.</div>
<svg class="abs" style="left:0;top:276px" width="758" height="26"><polygon points="208,0 758,0 758,10 695,19 595,6 237,24" fill="var(--red)"/></svg>

<!-- form card -->
<div class="abs card"></div>
<div class="abs eyebrow"><i></i>GET AN APPOINTMENT</div>
<div class="abs card-title">Leave A Message</div>
<div class="abs card-copy">Lorem ipsum dolor sit amet, consectetur adipiscing elit, sed do eius tempor incididunt ut labore etdolore.</div>

<div class="abs field filled" style="left:94px;top:470px;width:150px;height:27px">Dana Ellery |<span class="field-icon" style="border-color:#333"><svg width="7" height="7" viewBox="0 0 8 8"><circle cx="4" cy="2.5" r="1.8" fill="#222"/><path d="M1 8a3 3 0 0 1 6 0z" fill="#222"/></svg></span></div>
<div class="abs field" style="left:249px;top:470px;width:150px;height:27px">+ 00 123 456 7890<span class="field-icon"><svg width="7" height="7" viewBox="0 0 12 12"><path d="M3 1.5l2 2.5-1.2 1.2a6 6 0 0 0 3 3L8 7l2.5 2-1.2 1.8C5.5 10.5 1.5 6.5 1.2 2.7z" fill="#999"/></svg></span></div>
<div class="abs field" style="left:94px;top:502px;width:150px;height:27px">info@danaellery.com<span class="field-icon"><svg width="7" height="6" viewBox="0 0 8 6"><rect x="0.5" y="0.5" width="7" height="5" fill="none" stroke="#999"/><path d="M.5 .5L4 3.3 7.5.5" fill="none" stroke="#999"/></svg></span></div>
<div class="abs field" style="left:249px;top:502px;width:150px;height:27px">Service<span class="field-icon"><svg width="6" height="4" viewBox="0 0 6 4"><path d="M.5.5L3 3 5.5.5" fill="none" stroke="#999"/></svg></span></div>
<div class="abs field area" style="left:94px;top:535px;width:305px;height:65px">Message<span class="field-icon"><svg width="7" height="7" viewBox="0 0 8 8"><path d="M1 7l1-3 4-4 2 2-4 4z" fill="#999"/></svg></span></div>

<svg class="abs submit" width="117" height="28"><polygon points="14,0 117,0 117,28 0,28 0,14" fill="var(--red)"/></svg>
<div class="abs submit-label"><svg width="9" height="9" viewBox="0 0 10 10"><path d="M0 5L10 0 7 10 5 6z" fill="#fff"/></svg>SUBMIT</div>

<!-- info column -->
<div class="abs lead">We're open for business 5 days a week. See<br>the <u>opening hours</u> of our workshop</div>
<div class="abs lead-copy">If you have any questions simply use the following contact details.</div>
<div class="abs touch-title">Have Questions?<br>Get In Touch!</div>
<div class="abs touch-copy">Great! We're excited to hear from you and let's start something special togerter. call us for any inquery.</div>

<div class="abs contact-row" style="top:516px">
  <span class="contact-icon"><svg width="9" height="11" viewBox="0 0 10 12"><path d="M5 0a4 4 0 0 1 4 4c0 3-4 8-4 8S1 7 1 4a4 4 0 0 1 4-4z" fill="#fff"/><circle cx="5" cy="4" r="1.5" fill="var(--red)"/></svg></span>
  <span>418 Harbor Ridge Way #3<br>Dunmore, TX 75210</span>
</div>
<div class="abs contact-row" style="top:544px">
  <span class="contact-icon"><svg width="10" height="7" viewBox="0 0 10 7"><rect width="10" height="7" rx="1" fill="#fff"/><path d="M.5.5L5 4 9.5.5" fill="none" stroke="var(--red)"/></svg></span>
  <span>hello@kestrelautoshop.com</span>
</div>
<div class="abs contact-row big" style="top:573px">
  <span class="contact-icon"><svg width="10" height="10" viewBox="0 0 12 12"><path d="M3 1.5l2 2.5-1.2 1.2a6 6 0 0 0 3 3L8 7l2.5 2-1.2 1.8C5.5 10.5 1.5 6.5 1.2 2.7z" fill="#fff"/></svg></span>
  <span>Office: 555.640.2218<br>Cell: 555.640.7391</span>
</div>
<div class="abs socials" style="left:448px;top:619px">
  <span class="social">f</span><span class="social">in</span><span class="social">ig</span>
</div>

<!-- map -->
<div class="abs band-soft"></div>
<div class="abs map" role="img" aria-label="Street map showing the shop location"></div>
<div class="abs map-card"><b>418 Harbor Ridge Way Ste 3</b><br>418 Harbor Ridge Way #3<br>Dunmore, TX 75210<br><span class="link" style="line-height:14px">View larger map</span></div>
<div class="abs map-dir"><svg width="7" height="7" viewBox="0 0 8 8"><path d="M4 0l4 4-4 4-4-4z" fill="#1a73e8"/></svg><br>Directions</div>
<div class="abs zoom">+<br>−</div>

<!-- footer -->
<div class="abs footer"></div>
<div class="abs foot-brand"><span class="brand-dot" style="width:16px;height:16px"></span><span class="brand-name">KESTREL</span></div>
<div class="abs foot-brand-sub">AUTOMOTIVE</div>
<div class="abs badge" style="left:72px;top:1095px;width:57px;height:22px"></div>
<div class="abs badge" style="left:131px;top:1095px;width:49px;height:22px"></div>
<div class="abs badge" style="left:72px;top:1119px;width:30px;height:22px"></div>
<div class="abs badge" style="left:104px;top:1119px;width:59px;height:22px"></div>

<div class="abs foot-title" style="left:232px">Quick Links.</div>
<div class="abs foot-links"><span>Home</span><span>About Us</span><span>Services</span><span>Gallery</span><span>Testimonials</span><span>Contact Us</span></div>

<div class="abs foot-title" style="left:326px">Contact Us</div>
<div class="abs foot-row" style="top:1013px">
  <span class="foot-icon"><svg width="7" height="9" viewBox="0 0 10 12"><path d="M5 0a4 4 0 0 1 4 4c0 3-4 8-4 8S1 7 1 4a4 4 0 0 1 4-4z" fill="#666"/><circle cx="5" cy="4" r="1.5" fill="#d9d9d9"/></svg></span>
  <span>418 Harbor Ridge Way #3<br>Dunmore, TX 75210</span>
</div>
<div class="abs foot-row" style="top:1043px">
  <span class="foot-icon"><svg width="8" height="8" viewBox="0 0 12 12"><path d="M3 1.5l2 2.5-1.2 1.2a6 6 0 0 0 3 3L8 7l2.5 2-1.2 1.8C5.5 10.5 1.5 6.5 1.2 2.7z" fill="#666"/></svg></span>
  <span><em>OFFICE:</em> 555.640.2218<br><em>Phone:</em> 555.640.7391</span>
</div>
<div class="abs foot-row" style="top:1076px">
  <span class="foot-icon"><svg width="8" height="6" viewBox="0 0 10 7"><rect width="10" height="7" rx="1" fill="#666"/><path d="M.5.5L5 4 9.5.5" fill="none" stroke="#d9d9d9"/></svg></span>
  <span>hello@kestrelautoshop.com</span>
</div>
<div class="abs foot-row" style="top:1105px">
  <span class="foot-icon"><svg width="9" height="9" viewBox="0 0 10 10"><circle cx="5" cy="5" r="4.5" fill="#666"/><path d="M5 2.5V5l1.8 1.2" fill="none" stroke="#d9d9d9" stroke-width="1"/></svg></span>
  <span><em>Hours of Operation:</em> M-F 8:30-6pm</span>
</div>
<div class="abs foot-map" role="img" aria-label="Small area map of the shop neighborhood"></div>

<svg class="abs bottom-bar" width="758" height="27"><polygon points="0,25 196,25 196,27 0,27" fill="#111"/><polygon points="215,2 758,2 758,27 198,27" fill="var(--red)"/><polygon points="212,0 219,0 201,27 194,27" fill="#ccc"/></svg>
<div class="abs foot-social"><span class="social">f</span><span class="social">in</span><span class="social">ig</span></div>
<div class="abs copyright">Copyright © 2024 Kestrel Automotive LLC. All Rights Reserved.</div>

</body>
</html>
```